Need Company, new truck. Need graphics to increase advertising, branding, and make the truck pop

Need to decal/add graphics to new Bulk Fuel Delivery Truck to increase awareness, branding, exposure and advertise our business. We deliver Bulk Diesel Fuel and Gasoline, would like to add graphics to gain attention and list our phone number to generate leads and awareness. I have attached pics of the truck and our Logo which is also on the door of the truck attached. I have also added a Gas/Diesel nozzle pic that may be incorporated into your design as a visual to what we do. Please mark truck up, sides and back with your ideas

Need extra days to review

```html
<!DOCTYPE html>
<html lang="en">
<head>
<meta charset="UTF-8">
<title>Ridgeline Fuels – Truck Rear Graphics</title>
<link rel="stylesheet" href="https://fonts.googleapis.com/css2?family=Arimo:wght@700&family=Montserrat:wght@500;700&display=swap">
<style>
  :root {
    --cream: #efe9d6;
    --brand-green: #2f8a3f;
    --panel-green: #3a8f44;
    --nozzle-green: #2c7d3a;
    --nozzle-dark: #1d1d1d;
    --white: #ffffff;
    --ink: #151515;
  }
  * { margin: 0; padding: 0; box-sizing: border-box; }
  html, body {
    width: 1200px;
    height: 1000px;
    overflow: hidden;
    background: var(--cream);
  }
  .truck-rear-graphics {
    position: relative;
    width: 1200px;
    height: 1000px;
    background: var(--cream);
  }
  .brand-name {
    position: absolute;
    top: 170px;
    left: 0;
    width: 1200px;
    text-align: center;
    font-family: "Arimo", Arial, sans-serif;
    font-weight: 700;
    font-size: 84px;
    letter-spacing: 1px;
    color: var(--brand-green);
  }
  .nozzle-art {
    position: absolute;
    left: 110px;
    top: 410px;
    width: 300px;
    height: 360px;
    border-radius: 28px;
    background: linear-gradient(160deg, var(--nozzle-green) 0%, var(--nozzle-green) 45%, var(--nozzle-dark) 100%);
  }
  .delivery-panel {
    position: absolute;
    left: 390px;
    top: 450px;
    width: 700px;
    height: 230px;
    border-radius: 26px;
    background: var(--panel-green);
    color: var(--white);
    font-family: "Montserrat", Arial, sans-serif;
    text-align: center;
    display: flex;
    flex-direction: column;
    justify-content: center;
  }
  .delivery-panel .service {
    font-weight: 500;
    font-size: 72px;
    letter-spacing: 4px;
    line-height: 1.05;
  }
  .delivery-panel .phone {
    font-weight: 700;
    font-size: 72px;
    letter-spacing: 4px;
    line-height: 1.05;
  }
  .tagline {
    position: absolute;
    left: 390px;
    top: 710px;
    width: 700px;
    text-align: center;
    font-family: "Montserrat", Arial, sans-serif;
    font-weight: 700;
    font-size: 29px;
    letter-spacing: 0.5px;
    color: var(--ink);
  }
</style>
</head>
<body>
  <main class="truck-rear-graphics">
    <h1 class="brand-name">RIDGELINE FUELS</h1>
    <div class="nozzle-art" role="img" aria-label="Illustration of a green fuel pump nozzle with black hose"></div>
    <section class="delivery-panel">
      <p class="service">FUEL DELIVERY</p>
      <p class="phone">604-555-0182</p>
    </section>
    <p class="tagline">HIGH QUALITY DIESEL AT A FAIR PRICE</p>
  </main>
</body>
</html>
```